Brantley Water Taxi and Transport

Need to redesign our business cards to relay that we do freight logistics and water taxi service. We also work with gov. agencies doing environmental clean up, oil spill response, remote site construction and work with many of the air taxi and helicopter services on Kodiak Island. Out website is www.brantleywatertaxi-example.com to get a better idea of what we do.

Contact Information for Business Card

I have a previous business card but it just has the logo on the front, and a sunset picture on the back with the contact info. It does not relay what we do and what we can help with. I like a simple straight forward design over a busy one.

Colors
3176b5
0455a3
cfdfed

Requirements
Must have
• logo, email, website, phone number

```html
<!DOCTYPE html>
<html lang="en">
<head>
<meta charset="utf-8">
<title>Brantley Water Taxi and Transport – Business Cards</title>
<link href="https://fonts.googleapis.com/css2?family=Montserrat:wght@400;500;600;700&display=swap" rel="stylesheet">
<style>
  :root {
    --page-bg: #c9c9c9;
    --card-bg: #eeeeed;
    --brand-blue: #1f3c9c;
    --sky-blue: #4aa9e0;
    --accent-orange: #f39c1e;
    --text-grey: #6b6b6b;
    --divider: #c4c4c4;
  }
  * { margin: 0; padding: 0; box-sizing: border-box; }
  html, body { width: 1200px; height: 1200px; overflow: hidden; }
  body {
    background: var(--page-bg);
    font-family: "Montserrat", sans-serif;
    position: relative;
  }
  .card {
    position: absolute;
    left: 226px;
    width: 780px;
    height: 452px;
    background: var(--card-bg);
    box-shadow: 0 6px 14px rgba(0,0,0,0.18);
  }
  .card--front { top: 106px; }
  .card--back { top: 638px; }

  /* Brand name lockup */
  .brand {
    position: absolute;
    display: flex;
    align-items: center;
    gap: 14px;
    color: var(--brand-blue);
    font-weight: 600;
  }
  .brand__dot {
    width: 34px; height: 34px;
    border-radius: 50%;
    background: var(--accent-orange);
    flex: none;
  }
  .card--front .brand {
    left: 0; right: 0; top: 128px;
    justify-content: center;
    font-size: 30px;
    line-height: 1.15;
  }
  .card--back .brand {
    left: 20px; width: 360px; top: 150px;
    flex-direction: column;
    text-align: center;
    font-size: 25px;
    line-height: 1.2;
    gap: 12px;
  }

  .tagline {
    position: absolute;
    left: 0; right: 0; top: 300px;
    text-align: center;
    color: var(--brand-blue);
    font-weight: 700;
    font-size: 19px;
  }
  .services {
    position: absolute;
    left: 0; right: 0;
    display: flex;
    justify-content: center;
    gap: 30px;
    list-style: none;
    color: var(--text-grey);
    font-size: 18px;
    letter-spacing: 0.3px;
  }
  .services--row1 { top: 344px; }
  .services--row2 { top: 384px; }
  .services li { display: flex; align-items: center; gap: 6px; }
  .services li::before {
    content: "";
    width: 9px; height: 9px;
    border-radius: 50%;
    background: var(--accent-orange);
  }

  .divider {
    position: absolute;
    left: 396px; top: 114px;
    width: 1px; height: 220px;
    background: var(--divider);
  }
  .contact {
    position: absolute;
    left: 426px; top: 108px;
    color: var(--text-grey);
    font-size: 17px;
  }
  .contact__name {
    color: var(--brand-blue);
    font-size: 27px;
    font-weight: 600;
    letter-spacing: 0.5px;
  }
  .contact__role {
    color: var(--accent-orange);
    font-size: 17px;
    margin-top: 2px;
  }
  .contact__address { margin-top: 30px; line-height: 29px; }
  .contact__lines { margin-top: 16px; line-height: 26px; font-size: 16px; }
  .contact__label { color: var(--brand-blue); font-weight: 600; }
  .contact__domain { color: var(--sky-blue); }
</style>
</head>
<body>

<section class="card card--front">
  <div class="brand">
    <span class="brand__dot"></span>
    <span>Brantley Water Taxi<br>and Transport</span>
  </div>
  <p class="tagline">Freight logistics and water taxi service</p>
  <ul class="services services--row1">
    <li>environmental clean up</li>
    <li>remote site constraction</li>
    <li>eco tourism</li>
  </ul>
  <ul class="services services--row2">
    <li>oil spill response</li>
    <li>much more</li>
  </ul>
</section>

<section class="card card--back">
  <div class="brand">
    <span class="brand__dot"></span>
    <span>Brantley Water Taxi<br>and Transport</span>
  </div>
  <div class="divider"></div>
  <div class="contact">
    <p class="contact__name">MARCUS HALE</p>
    <p class="contact__role">Owner</p>
    <p class="contact__address">740 Harbor View Rd., Suite 12<br>Alaska, Harbor Point</p>
    <p class="contact__lines">
      <span class="contact__label">P</span>: 907-555-0148<br>
      <span class="contact__label">E</span>: brantleywatertaxi@example.com<br>
      <span class="contact__label">W</span>: www.<span class="contact__domain">brantleywatertaxi-example</span>.com
    </p>
  </div>
</section>

</body>
</html>
```